" Oferecemos diagnósticos para definir os pontos de oportunidade de melhoria, depois elaboramos um projeto que começa pela criação de indicadores (que mostram o desempenho mês a mês) e ajudamos o cliente e elaborar um plano de ação para melhorar os indicadores, assim garantimos que os resultados melhorem de forma consistente e real. Garantimos o resultado se o cliente se envolver e executar as ações. Pois nosso negócio é entregar resultados. "

```html
<!DOCTYPE html>
<html lang="pt-BR">
<head>
<meta charset="utf-8">
<title>Indicare – Papel timbrado</title>
<link rel="stylesheet" href="https://fonts.googleapis.com/css2?family=Open+Sans:wght@400;600;700&display=swap">
<style>
  :root {
    --backdrop: #e6e7ea;
    --paper: #ffffff;
    --ink: #3a3f47;
    --brand-navy: #1d2a5a;
    --brand-blue: #1a9fd8;
    --brand-deep: #0b5fa8;
    --soft-grey: #eef0f2;
    --watermark-grey: #eceef1;
  }
  html, body {
    margin: 0;
    width: 1200px;
    height: 1200px;
    overflow: hidden;
    background: var(--backdrop);
    font-family: "Open Sans", Arial, sans-serif;
  }
  .letterhead {
    position: absolute;
    left: 211px;
    top: 50px;
    width: 778px;
    height: 1100px;
    background: var(--paper);
    box-shadow: 0 6px 24px rgba(0,0,0,0.12);
    overflow: hidden;
  }
  .letterhead__watermark {
    position: absolute;
    left: 240px;
    top: 200px;
    width: 500px;
    height: 680px;
    background: radial-gradient(ellipse at 60% 45%, var(--watermark-grey) 0%, rgba(236,238,241,0.5) 45%, rgba(255,255,255,0) 75%);
  }
  .brand {
    position: absolute;
    top: 74px;
    right: 70px;
    display: flex;
    align-items: center;
    gap: 12px;
  }
  .brand__dot {
    width: 26px;
    height: 26px;
    border-radius: 50%;
    background: var(--brand-blue);
  }
  .brand__name {
    font-size: 40px;
    font-weight: 700;
    line-height: 1.1;
    color: var(--brand-navy);
    letter-spacing: 0.5px;
  }
  .contact-bar {
    position: absolute;
    left: 60px;
    right: 60px;
    bottom: 118px;
    display: flex;
    justify-content: space-between;
    align-items: flex-start;
    font-size: 14px;
    color: var(--ink);
  }
  .contact-bar__item {
    display: flex;
    align-items: flex-start;
    gap: 8px;
    line-height: 1.35;
    white-space: nowrap;
  }
  .contact-bar__icon {
    width: 16px;
    height: 16px;
    flex: none;
    margin-top: 1px;
  }
  .letterhead__footer-band {
    position: absolute;
    left: 0;
    bottom: 0;
    width: 100%;
    height: 100px;
  }
</style>
</head>
<body>
  <main class="letterhead">
    <div class="letterhead__watermark" role="img" aria-label="Faint brand watermark area in light grey"></div>

    <div class="brand">
      <span class="brand__dot"></span>
      <span class="brand__name">Indicare</span>
    </div>

    <footer class="contact-bar">
      <div class="contact-bar__item">
        <svg class="contact-bar__icon" viewBox="0 0 16 16" aria-hidden="true">
          <circle cx="8" cy="8" r="6.5" fill="none" stroke="var(--ink)" stroke-width="1.3"/>
          <ellipse cx="8" cy="8" rx="3" ry="6.5" fill="none" stroke="var(--ink)" stroke-width="1.1"/>
          <line x1="1.5" y1="8" x2="14.5" y2="8" stroke="var(--ink)" stroke-width="1.1"/>
        </svg>
        <span>www.indicare.com.br</span>
      </div>
      <div class="contact-bar__item">
        <svg class="contact-bar__icon" viewBox="0 0 16 16" aria-hidden="true">
          <path d="M8 1a5 5 0 0 0-5 5c0 3.6 5 9 5 9s5-5.4 5-9a5 5 0 0 0-5-5z" fill="var(--ink)"/>
          <circle cx="8" cy="6" r="1.8" fill="var(--paper)"/>
        </svg>
        <span>Rua das Acácias, 120<br>Centro – São Paulo</span>
      </div>
      <div class="contact-bar__item">
        <svg class="contact-bar__icon" viewBox="0 0 16 16" aria-hidden="true">
          <path d="M4 1.5l2.2 3-1.4 1.6c.8 1.8 2.3 3.3 4.1 4.1l1.6-1.4 3 2.2-1 2.5C7.5 13.5 2.5 8.5 1.5 3.5z" fill="var(--ink)"/>
        </svg>
        <span>(11) 4000-0000</span>
      </div>
    </footer>

    <svg class="letterhead__footer-band" viewBox="0 0 778 100" preserveAspectRatio="none" aria-hidden="true">
      <defs>
        <linearGradient id="bandBlue" x1="0" y1="0" x2="1" y2="0">
          <stop offset="0" stop-color="var(--brand-blue)"/>
          <stop offset="0.6" stop-color="#2bb3e6"/>
          <stop offset="1" stop-color="var(--brand-deep)"/>
        </linearGradient>
      </defs>
      <rect x="0" y="0" width="778" height="100" fill="var(--soft-grey)" opacity="0.6"/>
      <path d="M0 10 L778 10 L778 16 L0 16 Z" fill="#d9dcdf"/>
      <path d="M0 40 L300 40 L340 60 L778 60 L778 100 L0 100 Z" fill="url(#bandBlue)"/>
      <path d="M0 28 L280 28 L320 48 L778 48 L778 54 L316 54 L276 34 L0 34 Z" fill="var(--brand-blue)" opacity="0.45"/>
    </svg>
  </main>
</body>
</html>
```